Book Cover, Virtual Assistant book (pop art?)

I'm writing my second book ( Mastering Remote Helpers - Hand Off Chores, Keep Creating Joy) and need a cover creating.

My previous book had a pop-art cover which makes it stand out. The books aren't a set, they are for different audiences. However, I'll obviously have both on my website and it would be nice if there was some theme that ties them together.

I'd like a main image and then a wrap around the front and back of a book (even if that's just the colour and a pattern on the back and spine).

The book is all about efficiency and organisation so the cover shouldn't be over fussy or complicated, this is all about making things easier.
Updates

Hello

I wasn't very clear but in this case "Virtual Assistant" is a human, not a robot!

thanks

Target Market(s)

This book will mostly be purchased by entrepreneurs, business owners and very busy people that are thinking about working with a Virtual Assistant. They will be smart, educated but also want to be entertained a little. It needs to appeal to both men and women. I run a VA agency and this will be used as a marketing tool.

Industry/Entity Type

Business support

Font styles to use
Decorative

Requirements
Must have
• An eye catching design.
Nice to have
• Based on the title of the book Mastering Remote Helpers - Hand Off Chores, Keep Creating Joy, I have thought about the word brilliance but I'm not married to it. My last book was a pop art cover and it might be nice to keep that theme in some way but again, not married to it. I've attached my business logo. Whilst it isn't written by the business it will be used for marketing so potentially the colours or style might be incorporated in some way. Teal HEX #199BAB 25 / 155 / 171 Coral HEX #EE786E 238 / 120/ 110
Should not have
• Any old fashioned "secretary type" images or generic stock pics of phones, typewriters etc. If it's a person image it should be modern and feisty. No robots please!

```html
<!DOCTYPE html>
<html lang="en">
<head>
<meta charset="utf-8">
<title>Mastering Remote Helpers – Book Cover</title>
<link rel="stylesheet" href="https://fonts.googleapis.com/css2?family=Open+Sans:wght@700;800&family=Allerta+Stencil&family=Kalam:wght@700&display=swap">
<style>
  :root {
    --ink: #111014;
    --white: #ffffff;
    --mustard: #f0c060;
    --rule: #f2b233;
    --brown: #6b2a1c;
    --teal: #199bab;
    --magenta: #b2418f;
    --violet: #5a3a8c;
    --orange: #f08a3c;
    --sky: #4fb6e6;
    --page: #dfe6ea;
  }
  * { margin: 0; padding: 0; box-sizing: border-box; }
  html, body { width: 800px; height: 1200px; overflow: hidden; background: var(--page); }
  .cover {
    position: relative;
    width: 800px;
    height: 1200px;
    overflow: hidden;
    background: var(--ink);
  }
  .cover-art {
    position: absolute;
    inset: 0;
    background:
      radial-gradient(circle at 30% 28%, rgba(255,255,255,0.55), transparent 22%),
      linear-gradient(150deg, var(--sky) 0%, var(--violet) 30%, var(--magenta) 52%, var(--orange) 72%, #3a2b3f 100%);
  }
  .imprint {
    position: absolute;
    top: 34px;
    right: 34px;
    width: 128px;
    height: 128px;
    background: var(--white);
    display: flex;
    flex-direction: column;
    align-items: center;
    justify-content: center;
    gap: 8px;
  }
  .imprint-mark { width: 34px; height: 34px; background: var(--teal); }
  .imprint-name {
    font-family: "Open Sans", sans-serif;
    font-weight: 700;
    font-size: 13px;
    letter-spacing: 0.5px;
    color: var(--teal);
    text-align: center;
    line-height: 1.1;
  }
  .title-rule {
    position: absolute;
    left: 64px;
    top: 430px;
    width: 330px;
    height: 7px;
    background: var(--rule);
  }
  .title {
    position: absolute;
    left: 60px;
    top: 450px;
    font-family: "Open Sans", sans-serif;
    font-weight: 800;
    color: var(--white);
    line-height: 0.95;
    letter-spacing: -1px;
    text-shadow: 0 3px 10px rgba(0,0,0,0.35);
  }
  .title span { display: block; }
  .title .small { font-size: 82px; }
  .title .big { font-size: 124px; }
  .tagline-panel {
    position: absolute;
    right: 0;
    bottom: 0;
    width: 470px;
    height: 360px;
    background: var(--ink);
  }
  .tagline {
    position: absolute;
    right: 36px;
    bottom: 40px;
    width: 400px;
    height: 280px;
    background: var(--mustard);
    display: flex;
    flex-direction: column;
    justify-content: center;
    padding-left: 34px;
    font-family: "Allerta Stencil", sans-serif;
    font-size: 40px;
    letter-spacing: 5px;
    line-height: 1.22;
    color: var(--brown);
  }
  .byline {
    position: absolute;
    left: 36px;
    bottom: 60px;
    width: 280px;
    height: 170px;
  }
  .byline svg { position: absolute; inset: 0; }
  .byline-text {
    position: absolute;
    left: 28px;
    top: 18px;
    font-family: "Kalam", cursive;
    font-weight: 700;
    font-size: 34px;
    line-height: 1.05;
    color: var(--brown);
    transform: rotate(-6deg);
  }
</style>
</head>
<body>
  <main class="cover">
    <div class="cover-art" role="img" aria-label="Pop-art halftone portrait of a modern virtual assistant wearing headphones at a laptop in a sunny window-lit office"></div>

    <div class="imprint">
      <div class="imprint-mark"></div>
      <div class="imprint-name">Nearby Assist</div>
    </div>

    <div class="title-rule"></div>
    <h1 class="title">
      <span class="small">mastering</span>
      <span class="big">remote</span>
      <span class="big">helpers</span>
    </h1>

    <div class="tagline-panel"></div>
    <p class="tagline">HAND OFF<br>CHORES,<br>KEEP CREATING<br>JOY</p>

    <div class="byline">
      <svg width="280" height="170" viewBox="0 0 280 170" aria-hidden="true">
        <path d="M20 8 H260 Q272 8 272 20 V112 Q272 124 260 124 H125 L105 162 L95 124 H20 Q8 124 8 112 V20 Q8 8 20 8 Z"
              fill="#ffffff" stroke="#111014" stroke-width="4"/>
      </svg>
      <p class="byline-text">by Helen<br>Marlowe</p>
    </div>
  </main>
</body>
</html>
```